Ferncrest Dental, LLC business card project

Business card to be designed with current logo.
Dental office- please keep design of card that looks clean and professional.
Please include the following info:
Ferncrest Dental, LLC
Dr. Lorna Pettigrew
2871 Marlowe Street
Larkhaven, NR 00917
555-555-0193
ferncrestdental.office@examplemail.test
Hello everyone-
Reason: Just got back from overseas- will look at all designs and provide feedback. Thank you!
Reason: Polling my friends for the final selection-
thank you to all those that participated- so many talented designers!

```html
<!DOCTYPE html>
<html lang="en">
<head>
<meta charset="utf-8">
<title>Ferncrest Dental, LLC – Business Card</title>
<link rel="stylesheet" href="https://fonts.googleapis.com/css2?family=Fira+Sans:wght@400;500&display=swap">
<style>
  :root {
    --sky-top: #ffffff;
    --sky-mid: #94bbea;
    --sky-low: #4f8ad8;
    --sky-bottom: #1a5fc6;
    --frame: #2a3340;
    --brand-lime: #72d40a;
    --name-green: #2f8a05;
    --contact-white: #ffffff;
    --mark-grey: #e6eaee;
  }
  html, body {
    margin: 0;
    padding: 0;
    width: 1200px;
    height: 741px;
    overflow: hidden;
    background: #ffffff;
  }
  .card {
    position: relative;
    width: 1200px;
    height: 741px;
    box-sizing: border-box;
    border: 2px solid var(--frame);
    background: linear-gradient(to bottom,
      var(--sky-top) 0%,
      var(--sky-top) 8%,
      var(--sky-mid) 45%,
      var(--sky-low) 75%,
      var(--sky-bottom) 100%);
    font-family: "Fira Sans", "Trebuchet MS", sans-serif;
    overflow: hidden;
  }
  .brand {
    position: absolute;
    left: 60px;
    top: 40px;
    display: flex;
    align-items: center;
    gap: 28px;
  }
  .brand-dot {
    display: block;
    width: 100px;
    height: 100px;
  }
  .brand-name {
    margin: 0;
    font-size: 82px;
    font-weight: 400;
    color: var(--brand-lime);
    letter-spacing: -1px;
    line-height: 1;
    white-space: nowrap;
  }
  .doctor {
    position: absolute;
    left: 0;
    right: 0;
    top: 240px;
    margin: 0;
    text-align: center;
    font-size: 84px;
    font-weight: 500;
    color: var(--name-green);
    letter-spacing: 2px;
    line-height: 1;
    white-space: nowrap;
  }
  .contact {
    position: absolute;
    margin: 0;
    color: var(--contact-white);
    font-weight: 400;
    line-height: 1;
    white-space: nowrap;
  }
  .contact-street { left: 384px; top: 370px; font-size: 58px; letter-spacing: 1px; }
  .contact-city   { left: 324px; top: 438px; font-size: 58px; letter-spacing: 1px; }
  .contact-phone  { left: 397px; top: 505px; font-size: 62px; }
  .contact-email  { left: 0; right: 0; top: 630px; text-align: center; font-size: 48px; }
</style>
</head>
<body>
  <div class="card">
    <header class="brand">
      <svg class="brand-dot" viewBox="0 0 100 100" aria-hidden="true">
        <circle cx="50" cy="50" r="48" fill="var(--mark-grey)"/>
      </svg>
      <h1 class="brand-name">Ferncrest Dental, LLC</h1>
    </header>

    <h2 class="doctor">Dr. Lorna Pettigrew</h2>

    <p class="contact contact-street">2871 Marlowe Street</p>
    <p class="contact contact-city">Larkhaven, NR 00917</p>
    <p class="contact contact-phone">555-555-0193</p>
    <p class="contact contact-email">ferncrestdental.office@examplemail.test</p>
  </div>
</body>
</html>
```